Real Estate For Sale Sign

I need to design a for sale sign. It needs to include The following information
Logo: Attached
Name: Corinne Vasquel,
Company Name: Gilded Harbor Real Estate,
Phone Number: 503-841-2096
BRE Licence Number 04817359 (Can Be small)
Sign size 24x30

I am not sure about including my website but I would like to see options with it. www.gildedharbor-example.com
Updates

Target Market(s)

Potential Buyers or Sellers of Real Estate. Must be easy to read.

Industry/Entity Type

Real Estate

Requirements
Must have
• I want it to feel luxurious and sharp.

```html
<!DOCTYPE html>
<html lang="en">
<head>
<meta charset="utf-8">
<title>Gilded Harbor Real Estate – For Sale Sign</title>
<link rel="stylesheet" href="https://fonts.googleapis.com/css2?family=Marcellus&family=Arimo:wght@400&display=swap">
<style>
  :root {
    --frame-black: #070707;
    --sign-white: #ffffff;
    --band-blue: #33a3ec;
    --sky-blue: #3aa8ee;
    --phone-blue: #2e9fe8;
    --brand-slate: #5f6f80;
    --logo-ring: #3f8fd8;
    --ink: #0c0c0c;
    --web-blue: #1e8fe0;
  }
  * { margin: 0; padding: 0; box-sizing: border-box; }
  html, body {
    width: 1200px; height: 1000px; overflow: hidden;
    background: var(--frame-black);
  }
  .sign {
    position: absolute; left: 0; top: 100px;
    width: 1200px; height: 745px;
    background: var(--sign-white);
    font-family: "Marcellus", serif;
  }
  .brand-mark {
    position: absolute; left: 105px; top: 55px;
  }
  .brand-name {
    position: absolute; left: 425px; top: 118px;
    color: var(--brand-slate);
    font-size: 64px; line-height: 1;
    letter-spacing: 1px;
  }
  .brand-name .brand-sub {
    display: block;
    margin-top: 18px; margin-left: 118px;
    font-size: 36px; letter-spacing: 9px;
  }
  .agent-band {
    position: absolute; left: 0; top: 372px;
    width: 1200px; height: 98px;
    background: var(--band-blue);
    display: flex; align-items: center; justify-content: center;
    padding-left: 30px;
    font-size: 62px; letter-spacing: 2px;
  }
  .agent-first { color: var(--sign-white); margin-right: 22px; }
  .agent-last { color: var(--ink); }
  .company-line {
    position: absolute; left: 0; top: 497px; width: 1200px;
    text-align: center; padding-left: 10px;
    font-size: 48px; letter-spacing: 2px; line-height: 1;
    color: var(--sky-blue);
  }
  .company-line .accent { color: var(--ink); }
  .phone {
    position: absolute; left: 0; top: 568px; width: 1200px;
    text-align: center; padding-right: 15px;
    font-size: 66px; letter-spacing: 2px; line-height: 1;
    color: var(--phone-blue);
  }
  .website {
    position: absolute; left: 22px; top: 710px;
    font-family: "Arimo", sans-serif;
    font-size: 15px; letter-spacing: 3.5px;
    color: var(--web-blue);
    text-transform: uppercase;
  }
  .licence {
    position: absolute; right: 30px; top: 700px;
    font-family: "Arimo", sans-serif;
    font-size: 26px; letter-spacing: 1px;
    color: var(--ink);
  }
</style>
</head>
<body>
  <main class="sign">
    <svg class="brand-mark" width="250" height="250" viewBox="0 0 250 250" aria-hidden="true">
      <circle cx="125" cy="125" r="112" fill="none" stroke="var(--logo-ring)" stroke-width="8"/>
    </svg>
    <div class="brand-name">GILDED HARBOR<span class="brand-sub">REAL ESTATE</span></div>

    <div class="agent-band">
      <span class="agent-first">CORINNE</span><span class="agent-last">VASQUEL</span>
    </div>

    <p class="company-line">GILDED <span class="accent">HARBOR</span> REAL ESTATE</p>
    <p class="phone">503-841-2096</p>

    <p class="website">www.gildedharbor-example.com</p>
    <p class="licence">BRE Licence Number 04817359</p>
  </main>
</body>
</html>
```